RW Frameworks Inc Business cards

We need business cards using our existing logo but slightly modified. Right now the logo says RW Framework Masonry. We want to keep the RW part of the design, but replace the Framework Masonry portion with "FRAMEWORKS". Please see the attached file.
Ideally this would be a blank template so we can add Different Names, titles, and phone numbers later.
On the one side we want only the logo and on the other side the detail. I'm attaching an example for you to see.
Please reach out with any other questions. Our address and other details will be given out once we find a design we like.

Target Market(s)

Construction Industry

```html
<!DOCTYPE html>
<html lang="en">
<head>
<meta charset="utf-8">
<title>RW Frameworks Inc – Business Cards</title>
<link rel="stylesheet" href="https://fonts.googleapis.com/css2?family=Arimo:wght@400;700&display=swap">
<style>
  :root {
    --backdrop: #d9d9d7;
    --card: #333336;
    --card-edge: #1f7ac9;
    --accent: #1f7ac9;
    --text-light: #f2f2f2;
    --emboss: #4a4a4e;
  }
  * { margin: 0; padding: 0; box-sizing: border-box; }
  html, body {
    width: 1200px; height: 900px; overflow: hidden;
    background: var(--backdrop);
    font-family: "Arimo", Arial, sans-serif;
  }
  .sheet {
    width: 1200px; height: 900px;
    display: flex; flex-direction: column; align-items: center; justify-content: center;
    gap: 40px;
  }
  .card {
    width: 700px; height: 400px;
    background: var(--card);
    border-bottom: 5px solid var(--card-edge);
    position: relative;
  }
  /* Front: details side */
  .card--details {
    display: flex; align-items: center;
  }
  .brand {
    width: 330px; display: flex; align-items: center; justify-content: center; gap: 14px;
  }
  .brand__square { width: 22px; height: 22px; background: var(--accent); }
  .brand__name {
    color: var(--text-light); font-weight: 700; font-size: 26px; letter-spacing: 4px;
  }
  .divider {
    width: 2px; height: 220px; background: var(--accent);
  }
  .details {
    padding-left: 36px; color: var(--text-light); font-size: 15px; line-height: 1.45;
  }
  .details__name { color: var(--accent); font-weight: 700; font-size: 22px; line-height: 1.1; }
  .details__title { margin-bottom: 14px; }
  .details__address { margin-bottom: 14px; }
  .contact { list-style: none; }
  .contact li { display: flex; align-items: center; gap: 9px; }
  .contact svg { width: 13px; height: 13px; fill: var(--text-light); flex: none; }
  /* Back: logo side */
  .card--logo { display: flex; align-items: center; justify-content: center; gap: 18px; }
  .card--logo .brand__square { width: 30px; height: 30px; background: var(--emboss); }
  .card--logo .brand__name { color: var(--emboss); font-size: 44px; letter-spacing: 7px; }
</style>
</head>
<body>
<main class="sheet">
  <section class="card card--details" aria-label="Business card, details side">
    <div class="brand">
      <span class="brand__square"></span>
      <span class="brand__name">RW FRAMEWORKS</span>
    </div>
    <div class="divider"></div>
    <div class="details">
      <p class="details__name">DANIEL HARPER</p>
      <p class="details__title">President</p>
      <p class="details__address">48 Millbrook Yard Road<br>Riverton NY 12840</p>
      <ul class="contact">
        <li><svg viewBox="0 0 16 16"><path d="M3.5 1l3 3-1.6 1.8a9 9 0 0 0 5.3 5.3L12 9.5l3 3-2 2.2C7.5 14.5 1.5 8.5 1.3 3z"/></svg>555-214-3960</li>
        <li><svg viewBox="0 0 16 16"><path d="M4 0h8a1 1 0 0 1 1 1v14a1 1 0 0 1-1 1H4a1 1 0 0 1-1-1V1a1 1 0 0 1 1-1zm1 2v10h6V2zm3 11a1 1 0 1 0 0 2 1 1 0 0 0 0-2z"/></svg>555-214-3870</li>
        <li><svg viewBox="0 0 16 16"><path d="M0 3h16v1.5L8 9 0 4.5zm0 3.2 8 4.5 8-4.5V13H0z"/></svg>info@rwframeworks-mail.com</li>
        <li><svg viewBox="0 0 16 16"><circle cx="8" cy="8" r="7"/></svg>www.rwframeworks-site.com</li>
      </ul>
    </div>
  </section>
  <section class="card card--logo" aria-label="Business card, logo side">
    <span class="brand__square"></span>
    <span class="brand__name">RW FRAMEWORKS</span>
  </section>
</main>
</body>
</html>
```